Financial Planner Marketing Post Card

I'm a Financial Planner and Managing Principal of our Washington DC office (we're a boutique firm based out of California).The name of my firm is The Wexmoor Group, LLC. We specialize in investment strategies and Estate Planning. We offer everything from Estate Planning to Education Planning to Risk Management along with Insurance Planning. But I want my post card to really highlight is the main product I'm trying to sell with are the Fiduciary Standards of Being a RAS (Registered Asset Steward). I will attach a file with the Fiduciary Standards, along with a list of my service and products, company logo, along with a personal slogan. I would like for there to be room on my post card for my photo as well. I would like to use both sides of the post card with color; along with room for the ADPS postage.

Boutique

```html
<!DOCTYPE html>
<html lang="en">
<head>
<meta charset="utf-8">
<title>Wexmoor Group Postcard</title>
<link href="https://fonts.googleapis.com/css2?family=Oswald:wght@300;400&family=Crimson+Text:wght@400;600;700&display=swap" rel="stylesheet">
<style>
  :root {
    --backdrop: #3f4042;
    --card: #ffffff;
    --ink: #1c1c1c;
    --navy: #1f4b6e;
    --teal: #2a97ae;
    --teal-deep: #376786;
    --teal-soft: #a9d5e1;
    --rule-light: #8a8a8a;
    --rule-dark: #2b2b2b;
  }
  * { margin: 0; padding: 0; box-sizing: border-box; }
  html, body { width: 1200px; height: 807px; overflow: hidden; }
  body { background: var(--backdrop); position: relative; font-family: "Crimson Text", Georgia, serif; color: var(--ink); }

  .postcard { position: absolute; left: 86px; top: 72px; width: 1025px; height: 663px; background: var(--card); }
  .postcard > * { position: absolute; }

  .portrait { left: 22px; top: 8px; width: 182px; height: 253px;
    background: linear-gradient(180deg, #e9e4df 0%, #8d8f93 45%, #55575c 100%);
    border-radius: 60px 60px 0 0; }

  .tagline { left: 183px; top: 43px; font-size: 17px; }
  .rule { height: 0; border-top: 1px solid var(--rule-light); }
  .rule-top { left: 166px; top: 73px; width: 506px; }
  .rule-mid { left: 38px; top: 261px; width: 634px; }
  .rule-bottom { left: 30px; top: 298px; width: 642px; border-top: 2px solid var(--rule-dark); }

  .acronym-band { left: 166px; top: 114px; width: 496px; height: 88px; border-radius: 44px;
    background: linear-gradient(90deg, var(--teal-deep) 0%, var(--teal-soft) 45%, var(--teal) 70%, var(--teal-soft) 100%); }
  .acronym { left: 166px; top: 126px; width: 496px; display: flex; justify-content: space-around;
    font-size: 46px; line-height: 60px; color: #fff; }

  .trait { font-family: "Oswald", "Arial Narrow", sans-serif; font-weight: 300; font-size: 15px; line-height: 20px;
    text-transform: uppercase; text-align: center; width: 140px; margin-left: -70px; color: #222; }
  .trait-above { top: 87px; }
  .trait-below { top: 212px; }

  .claim { left: 42px; top: 270px; font-size: 19px; font-weight: 700; letter-spacing: 0.3px; }

  .standards-title { left: 47px; top: 316px; font-size: 18px; font-weight: 700; color: var(--teal); }
  .standards { left: 42px; top: 346px; width: 380px; list-style: none; font-size: 15.5px; line-height: 18px; }
  .standards li { position: relative; padding-left: 17px; margin-bottom: 8px; }
  .standards svg { position: absolute; left: 0; top: 4px; }

  .sender { left: 707px; top: 106px; color: var(--navy); }
  .brand { font-size: 13px; font-weight: 700; letter-spacing: 0.2px; }
  .address { font-size: 15px; line-height: 17px; margin-top: 8px; font-style: normal; }

  .stamp-box { left: 908px; top: 35px; width: 97px; height: 106px; border: 1px solid #8a8a8a; }

  .mail-line { left: 722px; width: 249px; border-top: 1px solid var(--rule-light); }
</style>
</head>
<body>
<main class="postcard">
  <div class="portrait" role="img" aria-label="Photo of the financial planner in a grey suit, arms crossed"></div>

  <p class="tagline">Add someone with HEIGHT to your personal team of professionals</p>
  <div class="rule rule-top"></div>

  <span class="trait trait-above" style="left:209px">Honest</span>
  <span class="trait trait-above" style="left:369px">Integrity</span>
  <span class="trait trait-above" style="left:532px">Hardworking</span>

  <div class="acronym-band" role="img" aria-label="Teal graphic band behind the word HEIGHT"></div>
  <p class="acronym"><span>H</span><span>E</span><span>I</span><span>G</span><span>H</span><span>T</span></p>

  <span class="trait trait-below" style="left:290px">Experienced<br>&amp; Educated</span>
  <span class="trait trait-below" style="left:452px">A Belief in<br>“Giving First”</span>
  <span class="trait trait-below" style="left:612px; top:215px">Trustworthy</span>

  <div class="rule rule-mid"></div>
  <h2 class="claim">DUE TO THE FACT THAT I’M 6’4”</h2>
  <div class="rule rule-bottom"></div>

  <h3 class="standards-title">Fiduciary Standards:</h3>
  <ul class="standards">
    <li><svg width="12" height="9" viewBox="0 0 12 9"><path d="M1 4.5 L4.5 8 L11 1" fill="none" stroke="var(--teal)" stroke-width="2.2"/></svg>To place the interests of clients ahead of the interests of the adviser and its personnel;</li>
    <li><svg width="12" height="9" viewBox="0 0 12 9"><path d="M1 4.5 L4.5 8 L11 1" fill="none" stroke="var(--teal)" stroke-width="2.2"/></svg>To act with the skill, loyalty, reasonable care, diligence, and good judgment of a professional;</li>
    <li><svg width="12" height="9" viewBox="0 0 12 9"><path d="M1 4.5 L4.5 8 L11 1" fill="none" stroke="var(--teal)" stroke-width="2.2"/></svg>To provide full and fair disclosure of all important facts;</li>
    <li><svg width="12" height="9" viewBox="0 0 12 9"><path d="M1 4.5 L4.5 8 L11 1" fill="none" stroke="var(--teal)" stroke-width="2.2"/></svg>To avoid conflicts of interest;</li>
    <li><svg width="12" height="9" viewBox="0 0 12 9"><path d="M1 4.5 L4.5 8 L11 1" fill="none" stroke="var(--teal)" stroke-width="2.2"/></svg>To not mislead clients;</li>
    <li><svg width="12" height="9" viewBox="0 0 12 9"><path d="M1 4.5 L4.5 8 L11 1" fill="none" stroke="var(--teal)" stroke-width="2.2"/></svg>To disclose all conflicts of interest to clients and fairly<br>manage, in the client’s favor, any unavoidable conflicts.</li>
  </ul>

  <div class="sender">
    <p class="brand">WEXMOOR GROUP, LLC</p>
    <address class="address">480 Harlow Street NW<br>Suite 310<br>Washington, DC&nbsp; 20010</address>
  </div>

  <div class="stamp-box"></div>

  <div class="mail-line" style="top:416px"></div>
  <div class="mail-line" style="top:478px"></div>
  <div class="mail-line" style="top:537px"></div>
</main>
</body>
</html>
```